Need Business Card for our Indian Grocery Store

Industry/Entity Type

Grocery Store

Contact Information for Business Card

Manoj Baweja
Director

Store Locations:

Alderbrook
482 Elm Parade
P: 03 9172 5843

Wexhill
613 Carlow Road
P: 03 9238 6014

email: kvtmarts@mailnest.example

Requirements
Must have
• Our logo Colours

```html
<!DOCTYPE html>
<html lang="en">
<head>
<meta charset="UTF-8">
<title>KVT Groceries &amp; Spices – Business Card</title>
<link href="https://fonts.googleapis.com/css2?family=Questrial&display=swap" rel="stylesheet">
<style>
  :root {
    --brand-red: #e01e26;
    --ink: #1d1d1d;
    --paper: #ffffff;
    --backdrop: #2f3435;
    --card-w: 840px;
    --card-h: 480px;
  }
  * { margin: 0; padding: 0; box-sizing: border-box; }
  html, body { width: 1200px; height: 1200px; overflow: hidden; }
  body {
    background: var(--backdrop);
    font-family: "Questrial", sans-serif;
    display: flex;
    flex-direction: column;
    align-items: center;
    justify-content: center;
    gap: 60px;
  }
  .card {
    position: relative;
    width: var(--card-w);
    height: var(--card-h);
    overflow: hidden;
    box-shadow: 0 12px 30px rgba(0,0,0,.35);
  }

  /* Front */
  .card-front {
    background: var(--brand-red);
    color: var(--paper);
    display: flex;
    flex-direction: column;
    align-items: center;
    justify-content: center;
    text-align: center;
  }
  .brand-name { font-size: 150px; line-height: 1; letter-spacing: 2px; }
  .brand-sub { font-size: 30px; letter-spacing: 6px; margin-top: 14px; }
  .brand-tagline { font-size: 20px; letter-spacing: 2px; margin-top: 10px; }

  /* Back */
  .card-back { background: var(--paper); color: var(--ink); }
  .back-brand {
    position: absolute; left: 50px; top: 34px;
    color: var(--brand-red); text-align: center;
  }
  .back-brand .brand-name { font-size: 84px; }
  .back-brand .brand-sub { font-size: 16px; letter-spacing: 3px; margin-top: 6px; }
  .back-brand .brand-tagline { font-size: 12px; letter-spacing: 1px; margin-top: 4px; }

  .divider { position: absolute; inset: 0; }

  .person {
    position: absolute; right: 40px; top: 210px; text-align: right;
  }
  .person-name { font-size: 34px; }
  .person-role { font-size: 24px; margin-top: 4px; }

  .store { position: absolute; font-size: 20px; line-height: 1.35; }
  .store-north { left: 60px; top: 246px; }
  .store-south { left: 430px; top: 330px; }
  .store-name {
    color: var(--brand-red); font-size: 22px;
    display: flex; align-items: center; gap: 8px;
  }
  .store-phone { display: flex; align-items: center; gap: 8px; }
  .icon { width: 16px; height: 16px; flex: none; fill: var(--brand-red); }

  .email-band {
    position: absolute; left: 0; bottom: 0;
    width: 400px; height: 72px;
    background: var(--brand-red); color: var(--paper);
    display: flex; align-items: center; gap: 10px;
    padding-left: 40px; font-size: 22px;
  }
  .email-band .icon { fill: var(--paper); }
</style>
</head>
<body>

  <section class="card card-front">
    <div class="brand-name">KVT</div>
    <div class="brand-sub">GROCERIES &amp; SPICES</div>
    <div class="brand-tagline">Fresh Quality Every Day</div>
  </section>

  <section class="card card-back">
    <div class="back-brand">
      <div class="brand-name">KVT</div>
      <div class="brand-sub">GROCERIES &amp; SPICES</div>
      <div class="brand-tagline">Fresh Quality Every Day</div>
    </div>

    <svg class="divider" width="840" height="480" viewBox="0 0 840 480" aria-hidden="true">
      <line x1="30" y1="205" x2="800" y2="310" stroke="#e01e26" stroke-width="2"/>
    </svg>

    <div class="person">
      <div class="person-name">Manoj Baweja</div>
      <div class="person-role">Director</div>
    </div>

    <div class="store store-north">
      <div class="store-name">
        <svg class="icon" viewBox="0 0 16 16"><path d="M8 0a5.5 5.5 0 0 0-5.5 5.5C2.5 10 8 16 8 16s5.5-6 5.5-10.5A5.5 5.5 0 0 0 8 0zm0 8a2.5 2.5 0 1 1 0-5 2.5 2.5 0 0 1 0 5z"/></svg>
        Alderbrook
      </div>
      <div class="store-street">482 Elm Parade</div>
      <div class="store-phone">
        <svg class="icon" viewBox="0 0 16 16"><path d="M3.6 1 6 3.6 4.7 5.6a9 9 0 0 0 5.7 5.7l2-1.3L15 12.4 13.2 15C6.5 15 1 9.5 1 2.8z"/></svg>
        03 9172 5843
      </div>
    </div>

    <div class="store store-south">
      <div class="store-name">
        <svg class="icon" viewBox="0 0 16 16"><path d="M8 0a5.5 5.5 0 0 0-5.5 5.5C2.5 10 8 16 8 16s5.5-6 5.5-10.5A5.5 5.5 0 0 0 8 0zm0 8a2.5 2.5 0 1 1 0-5 2.5 2.5 0 0 1 0 5z"/></svg>
        Wexhill
      </div>
      <div class="store-street">613 Carlow Road</div>
      <div class="store-phone">
        <svg class="icon" viewBox="0 0 16 16"><path d="M3.6 1 6 3.6 4.7 5.6a9 9 0 0 0 5.7 5.7l2-1.3L15 12.4 13.2 15C6.5 15 1 9.5 1 2.8z"/></svg>
        03 9238 6014
      </div>
    </div>

    <div class="email-band">
      <svg class="icon" viewBox="0 0 16 16"><path d="M0 3h16v1.2L8 9 0 4.2zM0 5.6l8 4.8 8-4.8V13H0z"/></svg>
      kvtmarts@mailnest.example
    </div>
  </section>

</body>
</html>
```